Online Consultancy Needs a New Logo & Business Card Design

Based on the new logo we just received from another contest here on Maketrove,

You'll find a few different versions of our logo as well as examples of business card designs we like in this folder:
==> https://share.plumvault.net/folderview?id=7Kq2WzTn4pLrXcv9BsHaYe1MoD5g&usp=sharing

We are considering two options:
- clean, black design
- clean, white/blue design

We're willing to consider both options.

We're considering adding some special effects to the cards when printing - emboss, rounded corners, etc.

However, please deliver a design WITHOUT round corners.

Target Market(s)

Successful business people, serious and older audience.

Industry/Entity Type

Business

Contact Information for Business Card

For the business card, I would like a minimalistic card with the logo on one side (perhaps in the middle) and the contact information on the other.

For the contact information please use:
Name: Peter Lund
Position: Founder
Email: peter.lund@korvim.com
Phone Number: +381 63 98 76 210
Website URL: www.korvim.com

Font styles to use
Serif
Sans Serif

Requirements
Must have
• Must fit in perfectly with our current website design.

```html
<!DOCTYPE html>
<html lang="en">
<head>
<meta charset="UTF-8">
<title>Korvim Business Card</title>
<link rel="stylesheet" href="https://fonts.googleapis.com/css2?family=Montserrat:wght@400;600&display=swap">
<style>
  :root {
    --page: #e8e5df;
    --card-dark: #3b3b3c;
    --card-dark-edge: #2f2f30;
    --silver-light: #f4f4f4;
    --silver-mid: #d6d6d6;
    --silver-deep: #a9a9a9;
    --ink: #3a3a3a;
    --ink-soft: #5c5c5c;
    --white: #ffffff;
  }
  html, body {
    margin: 0;
    padding: 0;
    width: 1070px;
    height: 1200px;
    overflow: hidden;
    background: var(--page);
    font-family: "Montserrat", Arial, sans-serif;
  }
  .canvas {
    position: relative;
    width: 1070px;
    height: 1200px;
  }
  .card {
    position: absolute;
    left: 115px;
    width: 840px;
    height: 480px;
    overflow: hidden;
    box-shadow: 0 14px 30px rgba(0,0,0,0.22);
  }
  .card-front { top: 80px; background: var(--card-dark); }
  .card-back { top: 640px; background: var(--silver-light); }

  .silver-band {
    position: absolute;
    top: 0;
    left: 590px;
    width: 92px;
    height: 100%;
    background: linear-gradient(90deg, var(--silver-deep), var(--silver-light) 45%, var(--silver-mid) 70%, var(--silver-deep));
  }
  .corner {
    position: absolute;
    width: 70px;
    height: 70px;
    border-color: var(--silver-mid);
    border-style: solid;
    border-width: 0;
  }
  .corner-top-right { top: 40px; right: 40px; border-top-width: 2px; border-right-width: 2px; }
  .corner-bottom-left { bottom: 40px; left: 40px; border-bottom-width: 2px; border-left-width: 2px; }

  .brand {
    position: absolute;
    display: flex;
    align-items: center;
    gap: 14px;
    color: var(--white);
    font-weight: 600;
    letter-spacing: 1px;
  }
  .brand-dot {
    width: 16px;
    height: 16px;
    border-radius: 50%;
    background: var(--white);
  }
  .card-front .brand { left: 170px; top: 200px; font-size: 64px; }
  .card-back .brand { right: 60px; top: 70px; font-size: 50px; }

  .back-shape {
    position: absolute;
    inset: 0;
  }
  .contact {
    position: absolute;
    left: 48px;
    bottom: 36px;
    color: var(--ink);
  }
  .contact-name {
    margin: 0;
    font-size: 22px;
    font-weight: 600;
    letter-spacing: 2px;
    text-transform: uppercase;
  }
  .contact-role {
    margin: 2px 0 16px;
    font-size: 14px;
    letter-spacing: 2px;
    text-transform: uppercase;
    color: var(--ink-soft);
  }
  .contact-list {
    list-style: none;
    margin: 0;
    padding: 0;
    font-size: 14px;
    color: var(--ink-soft);
  }
  .contact-list li {
    display: flex;
    align-items: center;
    gap: 10px;
    margin-bottom: 7px;
  }
  .contact-list svg { width: 18px; height: 18px; flex: none; }
</style>
</head>
<body>
<main class="canvas">

  <section class="card card-front" aria-label="Card front">
    <div class="silver-band"></div>
    <div class="corner corner-top-right"></div>
    <div class="corner corner-bottom-left"></div>
    <div class="brand"><span class="brand-dot"></span><span>korvim</span></div>
  </section>

  <section class="card card-back" aria-label="Card back">
    <svg class="back-shape" viewBox="0 0 840 480" preserveAspectRatio="none">
      <defs>
        <linearGradient id="silverFade" x1="0" y1="0" x2="1" y2="1">
          <stop offset="0" stop-color="#c9c9c9"/>
          <stop offset="0.45" stop-color="#f5f5f5"/>
          <stop offset="1" stop-color="#d9d9d9"/>
        </linearGradient>
      </defs>
      <rect width="840" height="480" fill="url(#silverFade)"/>
      <polygon points="0,0 840,0 840,250 0,170" fill="#3b3b3c"/>
      <line x1="0" y1="170" x2="840" y2="250" stroke="#ffffff" stroke-opacity="0.5" stroke-width="2"/>
    </svg>

    <div class="brand"><span class="brand-dot"></span><span>korvim</span></div>

    <div class="contact">
      <p class="contact-name">Peter Lund</p>
      <p class="contact-role">Founder</p>
      <ul class="contact-list">
        <li>
          <svg viewBox="0 0 18 18"><circle cx="9" cy="9" r="9" fill="#4a4a4a"/><path d="M6 5l2 2-1 1.2c.6 1.2 1.5 2.1 2.8 2.8L11 10l2 2-1.2 1.3C9 13 5 9 4.7 6.2z" fill="#fff"/></svg>
          +381 63 98 76 210
        </li>
        <li>
          <svg viewBox="0 0 18 18"><circle cx="9" cy="9" r="9" fill="#4a4a4a"/><rect x="4.5" y="5.5" width="9" height="7" fill="none" stroke="#fff" stroke-width="1.2"/><path d="M4.5 5.5l4.5 4 4.5-4" fill="none" stroke="#fff" stroke-width="1.2"/></svg>
          peter.lund@korvim.com
        </li>
        <li>
          <svg viewBox="0 0 18 18"><circle cx="9" cy="9" r="9" fill="#4a4a4a"/><circle cx="9" cy="9" r="4.5" fill="none" stroke="#fff" stroke-width="1.1"/><path d="M4.5 9h9M9 4.5c-2 2.5-2 6.5 0 9M9 4.5c2 2.5 2 6.5 0 9" fill="none" stroke="#fff" stroke-width="1"/></svg>
          www.korvim.com
        </li>
        <li>
          <svg viewBox="0 0 18 18"><circle cx="9" cy="9" r="9" fill="#4a4a4a"/><path d="M9 14s-3.5-4-3.5-6.3a3.5 3.5 0 017 0C12.5 10 9 14 9 14z" fill="#fff"/><circle cx="9" cy="7.7" r="1.2" fill="#4a4a4a"/></svg>
          14 Harbor Lane, Novi Sad
        </li>
      </ul>
    </div>
  </section>

</main>
</body>
</html>
```